Elegant Business Card for Technology Company

Client is a supplier of innovative industrial communications and automation equipment since 2002. This contest is to gather fresh ideas for a redesign of the existing business card. Client is looking for design that best communicates tagline "Industrial Networking and Computing Specialist".

Design submissions should look modern, clean, elegant and professional. It should not be cluttered. Use white as the primary colour. Orange and black as secondary colour. Refer to jpeg File 1 on the current design.

Fonts used by Client used include Arial Regular, Arial Black, Roboto Regular, Roboto Black and Lato.

The winning design will be sent for offset printing using super white 250gsm artcard paper (open for suggestions).

Target Market(s)

System Engineers, Project Managers, Purchasing Managers from companies providing engineering services for Smart Cities.

Industry/Entity Type

Information Technology

Contact Information for Business Card

Refer to PDF File 3 for Business Card Details. Priority of short contact information would be as follows Name > Job Title > Email > Mobile > Web > Tel > Fax > Business Address >UEN (UEN represents company registration number)

Font styles to use
Sans Serif

Colors
ffffff
f37122
000000
5c5c5c

Requirements
Must have
• Refer to AI File 2 (Company Logo) & PDF File 3 (Information on Namecard)
Should not have
• No QR codes
• No Social Media Icons
• Do not create full Black or Orange colour background

```html
<!DOCTYPE html>
<html lang="en">
<head>
<meta charset="utf-8">
<title>KVS Business Card</title>
<link rel="stylesheet" href="https://fonts.googleapis.com/css2?family=Roboto:wght@400;500;900&display=swap">
<style>
  :root {
    --white: #ffffff;
    --orange: #f37122;
    --orange-deep: #c85716;
    --black: #111111;
    --grey: #5c5c5c;
    --backdrop: #e8e5e0;
  }
  * { box-sizing: border-box; margin: 0; padding: 0; }
  html, body {
    width: 1200px; height: 950px; overflow: hidden;
    background: var(--backdrop);
    font-family: "Roboto", Arial, sans-serif;
  }
  .stage {
    width: 1200px; height: 950px;
    display: flex; flex-direction: column; align-items: center; justify-content: center;
    gap: 50px;
  }
  .card {
    position: relative; width: 700px; height: 400px; overflow: hidden;
    box-shadow: 0 6px 18px rgba(0,0,0,.18);
  }
  /* Front */
  .card-front { background: var(--white); }
  .card-front .band { position: absolute; inset: 0; }
  .brand {
    position: absolute; display: flex; align-items: center; gap: 14px;
  }
  .brand-mark { width: 58px; height: 58px; border-radius: 50%; background: var(--orange); }
  .brand-name { font-weight: 900; font-size: 64px; letter-spacing: 2px; line-height: 1; }
  .card-front .brand { left: 50%; top: 62px; transform: translateX(-50%); }
  .card-front .brand-name { color: var(--black); }
  .contact {
    position: absolute; left: 0; right: 0; top: 252px;
    display: flex; flex-direction: column; align-items: center; gap: 9px;
    color: var(--white); font-size: 15px;
  }
  .contact-name { font-size: 20px; }
  .person { color: var(--orange); font-weight: 500; letter-spacing: 1px; }
  .divider { margin: 0 8px; }
  .role { letter-spacing: .5px; }
  .contact-row { display: flex; align-items: center; gap: 16px; }
  .item { display: flex; align-items: center; gap: 6px; }
  .icon { width: 15px; height: 15px; fill: var(--orange); }
  .address { font-size: 14px; }
  /* Back */
  .card-back { background: linear-gradient(135deg, var(--orange) 0%, var(--orange-deep) 100%); }
  .card-back .brand { left: 50%; top: 110px; transform: translateX(-50%); }
  .card-back .brand-mark { background: var(--white); opacity: .9; }
  .card-back .brand-name { color: var(--white); }
  .tagline {
    position: absolute; left: 0; right: 0; top: 210px;
    text-align: center; color: var(--white); font-size: 17px; line-height: 1.55;
  }
  .tagline-lead { font-weight: 500; }
</style>
</head>
<body>
<main class="stage">
  <section class="card card-front">
    <svg class="band" viewBox="0 0 700 400" width="700" height="400" aria-hidden="true">
      <path d="M0,236 Q340,188 700,204 L700,400 L0,400 Z" fill="#111111"/>
      <path d="M0,248 Q340,200 676,216 L676,400" fill="none" stroke="#f37122" stroke-width="4" stroke-linecap="round" stroke-dasharray="0 11"/>
    </svg>
    <div class="brand">
      <span class="brand-mark"></span>
      <span class="brand-name">KVS</span>
    </div>
    <div class="contact">
      <p class="contact-name"><span class="person">DANIEL LIM</span><span class="divider">|</span><span class="role">SALES MANAGER</span></p>
      <p class="contact-row">
        <span class="item"><svg class="icon" viewBox="0 0 16 16"><rect x="2" y="6" width="12" height="8" rx="1"/><rect x="4" y="1" width="8" height="6"/></svg>+65 6123 4580</span>
        <span class="item"><svg class="icon" viewBox="0 0 16 16"><path d="M1 6 Q8 0 15 6 L12 8 L10 6 L6 6 L4 8 Z M3 10 H13 V15 H3 Z"/></svg>+65 6123 4570</span>
        <span class="item"><svg class="icon" viewBox="0 0 16 16"><path d="M4 0 H12 V16 H4 Z M5.5 2 V12 H10.5 V2 Z"/></svg>+65 9123 4567</span>
      </p>
      <p class="contact-row">
        <span class="item"><svg class="icon" viewBox="0 0 16 16"><path d="M1 3 H15 V13 H1 Z M2 4 L8 9 L14 4 Z" fill-rule="evenodd"/></svg>sales@kvs.com.sg</span>
        <span class="item"><svg class="icon" viewBox="0 0 16 16"><circle cx="8" cy="8" r="7"/><path d="M1 8 H15 M8 1 Q4 8 8 15 M8 1 Q12 8 8 15" stroke="#111" stroke-width="1" fill="none"/></svg>www.kvs.com.sg</span>
      </p>
      <p class="address">24 Harbour Crescent, Tekpoint #05-12 (Lobby B), Singapore 409112</p>
    </div>
  </section>

  <section class="card card-back">
    <div class="brand">
      <span class="brand-mark"></span>
      <span class="brand-name">KVS</span>
    </div>
    <div class="tagline">
      <p class="tagline-lead">Industrial Networking &amp; Computing Specialist</p>
      <p>Ethernet / Wireless / Cellular</p>
      <p>Switching / Serial / Fieldbus Connectivity</p>
      <p>Remote Automation</p>
    </div>
  </section>
</main>
</body>
</html>
```